Fresh, modern, fun business card for pediatric dental practice

Need a business card for fresh, modern, fun pediatric dental practice

Clean look that matches our website's font and colors

We prefer the look of curved corners on business cards

Target Market(s)

parents (mothers) of young children, professionals, mid-high class

Industry/Entity Type

Dental

Contact Information for Business Card

Maplewood Pediatric Dentistry
482 Corbett Lane
Suite 619
Dellsford, PA 17392
717.555.0193
www.maplewoodtotsdental.example

Mei-Hua Tran, DMD
Colette Margrave, DMD
(we are working on our email address, but we would like that on the card as well)

Font styles to use
Sans Serif

Requirements
Must have
• All info; we would also like to make cards for individual staff members
• colors from our website and color palatte, attatched
• use same font and design as website for branding
Nice to have
• clean, simple card that has a pop of color
• we would like to see a few designs with our tag line "where smiles get brighter"
• we are not sure if we want to have it on there or not
• we would like to see a few designs incorporating the ribbon graphic on our website where the word WELCOME is

```html
<!DOCTYPE html>
<html lang="en">
<head>
<meta charset="utf-8">
<title>Maplewood Pediatric Dentistry – Business Card</title>
<link href="https://fonts.googleapis.com/css2?family=Open+Sans:wght@400;600;700&display=swap" rel="stylesheet">
<style>
  :root {
    --magenta: #c93a93;
    --gold: #e8ac2e;
    --gold-soft: #f3c65f;
    --ink: #4a4a4a;
    --paper: #ffffff;
    --backdrop: #2a2a2c;
  }
  * { box-sizing: border-box; margin: 0; padding: 0; }
  html, body {
    width: 1200px; height: 904px; overflow: hidden;
    background: var(--backdrop);
    font-family: "Open Sans", sans-serif;
  }
  .card {
    position: absolute;
    width: 680px; height: 389px;
    border-radius: 28px;
    overflow: hidden;
    box-shadow: 0 12px 30px rgba(0,0,0,.45);
  }
  /* Front */
  .card-front { left: 110px; top: 50px; background: var(--magenta); }
  .front-sun {
    position: absolute; left: 70px; top: 50px;
    width: 290px; height: 290px; border-radius: 50%;
    background: radial-gradient(circle, var(--gold-soft) 0%, var(--gold) 55%, rgba(232,172,46,0) 72%);
    opacity: .9;
  }
  .front-brand {
    position: absolute; right: 46px; top: 150px;
    display: flex; align-items: center; gap: 14px;
  }
  .brand-dot { width: 22px; height: 22px; border-radius: 50%; background: var(--gold); flex: none; }
  .brand-name {
    color: var(--gold); font-weight: 700; font-size: 30px; line-height: 1.1;
  }
  .brand-name span { display: block; font-size: 20px; }

  /* Back */
  .card-back { left: 410px; top: 475px; background: var(--paper); }
  .doctors {
    position: absolute; right: 40px; top: 34px; text-align: right;
    color: var(--magenta); font-weight: 700; font-size: 19px; line-height: 1.3;
  }
  .back-sun {
    position: absolute; right: 36px; top: 130px;
    width: 200px; height: 200px; border-radius: 50%;
    background: radial-gradient(circle, var(--gold-soft) 0%, var(--gold) 50%, rgba(232,172,46,0) 72%);
    opacity: .85;
  }
  .back-brand {
    position: absolute; left: 44px; top: 62px;
    display: flex; align-items: center; gap: 12px;
  }
  .back-brand .brand-name { font-size: 28px; }
  .details { position: absolute; left: 44px; top: 180px; color: var(--ink); font-size: 16px; line-height: 1.45; }
  .practice { color: var(--gold); font-weight: 700; font-size: 17px; }
  .contacts { list-style: none; margin-top: 14px; }
  .contacts li { display: flex; align-items: center; gap: 10px; white-space: nowrap; }
  .contacts svg { width: 18px; height: 18px; flex: none; }
</style>
</head>
<body>

<section class="card card-front">
  <div class="front-sun" role="img" aria-label="Large sun decoration in gold"></div>
  <div class="front-brand">
    <div class="brand-dot"></div>
    <div class="brand-name">Maplewood<span>Pediatric Dentistry</span></div>
  </div>
</section>

<section class="card card-back">
  <div class="doctors">
    <p>Mei-Hua Tran, DMD</p>
    <p>Colette Margrave, DMD</p>
  </div>
  <div class="back-sun" role="img" aria-label="Large sun decoration in gold"></div>

  <div class="back-brand">
    <div class="brand-dot"></div>
    <div class="brand-name">Maplewood<span>Pediatric Dentistry</span></div>
  </div>

  <div class="details">
    <p class="practice">Maplewood Pediatric Dentistry</p>
    <p>482 Corbett Lane</p>
    <p>Suite 619, Dellsford, PA 17392</p>
    <ul class="contacts">
      <li>
        <svg viewBox="0 0 20 20"><circle cx="10" cy="10" r="10" fill="var(--magenta)"/><path d="M6.5 5.5l2 .2.8 2.3-1.2 1a6 6 0 0 0 3 3l1-1.2 2.3.8.2 2c-4.5.7-8.7-3.5-8.1-8.1z" fill="#fff"/></svg>
        717.555.0193
      </li>
      <li>
        <svg viewBox="0 0 20 20"><circle cx="10" cy="10" r="10" fill="var(--magenta)"/><rect x="5" y="6.5" width="10" height="7" fill="#fff"/><path d="M5 6.5l5 4 5-4" stroke="var(--magenta)" stroke-width="1.2" fill="none"/></svg>
        meihua.tran@maplewoodtotsdental.example
      </li>
      <li>
        <svg viewBox="0 0 20 20"><circle cx="10" cy="10" r="10" fill="var(--magenta)"/><circle cx="10" cy="10" r="5" fill="none" stroke="#fff" stroke-width="1.3"/><path d="M5 10h10M10 5c-2.5 3-2.5 7 0 10M10 5c2.5 3 2.5 7 0 10" stroke="#fff" stroke-width="1.1" fill="none"/></svg>
        www.maplewoodtotsdental.example
      </li>
    </ul>
  </div>
</section>

</body>
</html>
```